Ranked amongst the Best Colleges and Programs

the size of the ad is Full Page, with bleed*
8”x 10.75" plus 0.25" bleed'
you have two choices for the tagline .. please chose what ever you think will allow you to make a better ad.
The instructions on the brief are in red
I am looking for a hight quality modern ad to place in local weekly publications that will stand out .
I would like a ad that people will look at and say i would like to see what this ad is all about.
I apprecate creative work.
the ad should not be very crowded and the text should be able to be read.
if you decide to use people in the ad .. (you don't have to ) then it should be a male dressed in white shirt in and sports jacket.. or if you would like you can use a vector and then use male or female people.
please leave one inch on the bottom for the footer

Target Market(s)

potential middle class students from 23-35 years of age

Industry/Entity Type

education

Requirements
Must have
• .the " 98% employment rate" should stand out in the ad.. but should not be the main part of the ad
Nice to have
• creative
Should not have
• Should not be a very busy or crowded ad.. i prefer pictures of men but should be .. in a business suit .. that looks professional- white shirt

```html
<!DOCTYPE html>
<html lang="en">
<head>
<meta charset="utf-8">
<title>NRU Masters of Accounting Degree</title>
<link rel="stylesheet" href="https://fonts.googleapis.com/css2?family=Montserrat:wght@600;700;800&family=Didact+Gothic&display=swap">
<style>
  :root {
    --red: #d4192f;
    --red-dark: #b30d17;
    --red-bright: #f6454a;
    --red-muted: #b5525c;
    --teal: #05a7bb;
    --teal-dark: #0f7f8c;
    --ink: #111111;
    --white: #ffffff;
    --panel: rgba(120, 146, 180, 0.72);
    --pink: #f7d3d6;
    --gold: #e7b84a;
  }
  * { margin: 0; padding: 0; box-sizing: border-box; }
  html, body { width: 873px; height: 1200px; overflow: hidden; background: var(--white); }
  .ad { position: relative; width: 873px; height: 1200px; overflow: hidden; background: var(--white); font-family: "Montserrat", sans-serif; }
  .backdrop { position: absolute; inset: 0; width: 873px; height: 1200px; }
  .headline { position: absolute; right: 38px; top: 24px; text-align: right; color: var(--red); font-weight: 700; line-height: 1; }
  .headline-main { font-size: 74px; letter-spacing: 1px; }
  .headline-sub { font-size: 33px; margin-top: 10px; letter-spacing: 0.5px; }
  .program-title { position: absolute; right: 38px; top: 158px; color: var(--white); font-weight: 700; font-size: 35px; letter-spacing: 0.3px; }
  .stat-ring { position: absolute; left: 26px; top: 296px; width: 210px; height: 206px; }
  .stat-value { position: absolute; left: 240px; top: 368px; font-family: "Didact Gothic", sans-serif; font-size: 86px; color: var(--teal-dark); line-height: 1; }
  .stat-label { position: absolute; left: 238px; top: 458px; font-family: "Didact Gothic", sans-serif; font-size: 28px; color: var(--ink); }
  .outcome-panel { position: absolute; left: 29px; top: 601px; width: 551px; height: 262px; background: var(--panel); border: 1px solid rgba(70, 90, 120, 0.6); border-radius: 8px; padding: 18px 20px 0 32px; }
  .outcome-panel p { font-family: "Didact Gothic", sans-serif; color: var(--white); font-size: 32.5px; line-height: 37px; text-shadow: 2px 2px 3px rgba(40, 50, 70, 0.7); }
  .ranked-label { position: absolute; left: 33px; top: 952px; width: 254px; height: 34px; background: var(--pink); font-weight: 700; font-size: 23px; color: var(--ink); padding-left: 16px; line-height: 34px; }
  .award { position: absolute; height: 68px; background: var(--red); border: 1px solid #7d0a12; border-radius: 0 34px 34px 0; color: var(--white); text-align: center; }
  .award-title { font-weight: 700; font-size: 16px; line-height: 18px; }
  .award-source { font-family: "Didact Gothic", sans-serif; font-size: 13px; }
  .award-colleges { left: 150px; top: 1024px; width: 226px; padding-top: 15px; padding-left: 34px; }
  .award-program { left: 520px; top: 1024px; width: 285px; padding-top: 9px; padding-left: 20px; }
  .seal { position: absolute; width: 124px; height: 124px; border-radius: 50%; background: radial-gradient(circle at 40% 35%, #f6dc8a, var(--gold) 55%, #b9862a); border: 6px solid var(--red); }
  .seal-one { left: 40px; top: 996px; }
  .seal-two { left: 409px; top: 996px; }
</style>
</head>
<body>
<div class="ad">
  <svg class="backdrop" viewBox="0 0 1649 2250" preserveAspectRatio="none" aria-hidden="false">
    <defs>
      <linearGradient id="officeGlow" x1="0" y1="0" x2="0" y2="1">
        <stop offset="0" stop-color="#ffffff"/>
        <stop offset="0.3" stop-color="#e9eef5"/>
        <stop offset="0.55" stop-color="#b9c9dc"/>
        <stop offset="1" stop-color="#eef1f6"/>
      </linearGradient>
      <linearGradient id="personTone" x1="0" y1="0" x2="0" y2="1">
        <stop offset="0" stop-color="#9a7a66"/>
        <stop offset="0.3" stop-color="#d8b09a"/>
        <stop offset="0.45" stop-color="#dcdcee"/>
        <stop offset="1" stop-color="#cfd2e8"/>
      </linearGradient>
    </defs>
    <g role="img" aria-label="Photo: smiling young professional man in white shirt and tie in a bright, blurred office">
      <rect x="0" y="780" width="1649" height="1285" fill="url(#officeGlow)"/>
      <path d="M1150 1000 Q1180 820 1330 815 Q1500 820 1520 1000 L1530 1260 Q1640 1300 1649 1360 L1649 2065 L1130 2065 L1150 1280 Q1170 1260 1190 1250 Z" fill="url(#personTone)"/>
    </g>
    <polygon class="band-shadow" points="815,395 1649,395 1649,440 860,440" fill="#b30d17"/>
    <polygon points="990,440 1560,440 1649,530 1649,755 1270,755" fill="#f6454a"/>
    <polygon points="1380,395 1649,395 1649,700" fill="#c7141c"/>
    <line x1="1270" y1="395" x2="1649" y2="760" stroke="#ffffff" stroke-width="3"/>
    <line x1="1370" y1="395" x2="1649" y2="660" stroke="#ffffff" stroke-width="3"/>
    <polygon points="1500,755 1649,755 1649,915" fill="#b5525c"/>
    <polygon points="0,1280 0,1890 210,1890" fill="#b5525c"/>
    <polygon points="0,1590 520,1590 840,1905 0,1905" fill="#f6454a"/>
    <polygon points="0,1380 0,1905 300,1905" fill="#c7141c" opacity="0.8"/>
    <line x1="0" y1="1420" x2="330" y2="1905" stroke="#ffffff" stroke-width="3"/>
    <line x1="0" y1="1520" x2="420" y2="1905" stroke="#ffffff" stroke-width="3"/>
    <rect x="0" y="1905" width="1560" height="160" fill="#b30d17"/>
    <polygon points="130,275 1649,275 1649,395 80,395" fill="#d4192f"/>
  </svg>

  <header class="headline">
    <div class="headline-main">GET AHEAD FASTER</div>
    <div class="headline-sub">IN YOUR CAREER WITH A PRESTIGIOUS</div>
  </header>
  <h1 class="program-title">NRU - MASTERS OF ACCOUNTING DEGREE</h1>

  <svg class="stat-ring" viewBox="0 0 210 206" role="img" aria-label="Pie chart: 98 percent employment rate">
    <path d="M3 101 A100 100 0 1 1 112 200" fill="none" stroke="var(--teal)" stroke-width="3"/>
    <path d="M109 13 A90 90 0 1 1 96 13.5 L99 51 A52 52 0 1 0 105 51 Z" fill="var(--teal)"/>
    <circle cx="103" cy="103" r="52" fill="var(--teal)"/>
    <circle cx="103" cy="103" r="45" fill="none" stroke="var(--white)" stroke-width="6"/>
    <text x="103" y="114" text-anchor="middle" font-family="Didact Gothic, sans-serif" font-size="29" fill="#ffffff">98%</text>
    <path d="M170 168 L190 201 L210 201" fill="none" stroke="var(--teal)" stroke-width="3"/>
  </svg>
  <svg style="position:absolute;left:215px;top:494px" width="262" height="6" aria-hidden="true"><line x1="0" y1="3" x2="262" y2="3" stroke="#05a7bb" stroke-width="3"/></svg>
  <div class="stat-value">98%</div>
  <div class="stat-label">Employment Rate</div>

  <section class="outcome-panel">
    <p>Northridge graduates have gone on to work in various high-quality jobs in top firms, earning impressive six-figure salaries as well as opening successful businesses.</p>
  </section>

  <div class="ranked-label">Ranked Amongst:</div>

  <div class="award award-colleges">
    <div class="award-title">Best Colleges</div>
    <div class="award-source">Ledger Review 2023</div>
  </div>
  <div class="award award-program">
    <div class="award-title">Best Master in Accounting Degree</div>
    <div class="award-source">Campus Index 2023</div>
  </div>
  <div class="seal seal-one" role="img" aria-label="Award seal"></div>
  <div class="seal seal-two" role="img" aria-label="Award seal"></div>
</div>
</body>
</html>
```